Crust Harbor Hotel Coupon

Would like to design a coupon that is for hotels' staff and to be dropped off at the hotel front office anytime someone calls from a hotel and as a Thank You for hotel staff for recommending us. Coupon value to be $ 2.00. Should say Thank You or Thank you for recommending us. Need our phone number 250 614 3750 on it. Color scheme to be Green and Red as in the attached logo. Coupon to be designed for printing size 3.5 inches high and 7.5 inches wide. Rear should say Fastest Delivery, Favourite Pizza for Sports teams etc. Ask for group deals. Attached logo to be on the coupon. Coupon should say coupon # and space left for us write number

```html
<!DOCTYPE html>
<html lang="en">
<head>
<meta charset="utf-8">
<title>Crust Harbor Coupon</title>
<link rel="stylesheet" href="https://fonts.googleapis.com/css2?family=Bitter:ital,wght@1,700&family=Roboto+Condensed:wght@500&family=Roboto:wght@300;400;700&display=swap">
<style>
  :root {
    --page-bg: #cccccc;
    --green-light: #4cb849;
    --green-mid: #219a3f;
    --green-dark: #0c7a34;
    --red: #ec1c24;
    --yellow: #f7b517;
    --white: #ffffff;
    --ink: #1a1a1a;
    --crust: #c9702a;
    --cheese: #f1d9a0;
  }
  * { margin: 0; padding: 0; box-sizing: border-box; }
  html, body {
    width: 1200px; height: 1200px; overflow: hidden;
    background: var(--page-bg);
  }
  .coupon {
    position: absolute; left: 32px; top: 316px;
    width: 1136px; height: 524px;
    background: linear-gradient(180deg, var(--green-light) 0%, var(--green-mid) 70%, var(--green-dark) 100%);
    font-family: "Roboto", Arial, sans-serif;
  }
  .cut-line {
    position: absolute; left: 21px; top: 20px; right: 19px; bottom: 20px;
    border: 2px dashed rgba(255,255,255,.85);
  }
  .brand {
    position: absolute; left: 44px; top: 72px;
    display: flex; align-items: center; gap: 12px;
  }
  .brand-dot { width: 34px; height: 34px; border-radius: 50%; background: var(--red); }
  .brand-name {
    font-family: "Roboto", Arial, sans-serif; font-weight: 700;
    font-size: 34px; color: var(--white); letter-spacing: .5px;
  }
  .value-badge { position: absolute; left: 365px; top: 26px; width: 160px; height: 160px; }
  .value-text {
    position: absolute; left: 365px; top: 26px; width: 160px; height: 160px;
    display: flex; align-items: center; justify-content: center;
    font-family: "Bitter", Georgia, serif; font-style: italic; font-weight: 700;
    color: var(--white); font-size: 50px; padding-right: 6px;
  }
  .value-text sup { font-size: 30px; position: relative; top: -14px; margin-left: 2px; }
  .coupon-number {
    position: absolute; left: 44px; top: 186px;
    display: flex; align-items: flex-end; gap: 16px;
    font-family: "Roboto Condensed", Arial, sans-serif; font-weight: 500;
    font-size: 60px; line-height: 1; color: var(--yellow);
  }
  .number-blank { width: 152px; border-bottom: 3px solid var(--yellow); margin-bottom: 6px; }
  .thanks {
    position: absolute; left: 44px; top: 262px; width: 560px;
    font-family: "Bitter", Georgia, serif; font-style: italic; font-weight: 700;
    color: var(--white); font-size: 50px; line-height: 58px;
  }
  .thanks .line1 { display: block; padding-left: 132px; }
  .thanks .line2 { display: block; white-space: nowrap; }
  .food-photo {
    position: absolute; left: 540px; top: 16px; width: 577px; height: 384px;
    border-radius: 48% 0 0 0 / 40% 0 0 0;
    background: radial-gradient(ellipse at 55% 50%, var(--cheese) 0%, #e6a95a 45%, #d35a2a 75%, var(--crust) 100%);
  }
  .info-band {
    position: absolute; left: 21px; top: 400px; width: 1096px; height: 104px;
    background: var(--red);
    border-top: 2px dashed rgba(255,255,255,.85);
    border-bottom: 2px dashed rgba(255,255,255,.85);
  }
  .call-icon { position: absolute; left: 32px; top: 20px; width: 60px; height: 60px; }
  .order {
    position: absolute; left: 110px; top: 16px; color: var(--white);
  }
  .order-label { font-weight: 300; font-size: 26px; line-height: 30px; }
  .order-phone { font-weight: 700; font-size: 35px; line-height: 40px; }
  .perks {
    position: absolute; right: 32px; top: 18px; width: 680px; text-align: right;
  }
  .perks-main { color: var(--white); font-size: 25px; line-height: 32px; }
  .perks-deal {
    color: var(--yellow); font-weight: 300; font-size: 30px; line-height: 40px;
    text-align: center; padding-left: 60px;
  }
</style>
</head>
<body>
<main class="coupon">
  <div class="cut-line"></div>

  <div class="brand">
    <span class="brand-dot"></span>
    <span class="brand-name">Crust Harbor</span>
  </div>

  <svg class="value-badge" viewBox="0 0 160 160" aria-hidden="true">
    <g fill="var(--red)" stroke="#ffffff" stroke-width="1">
      <rect x="23.5" y="23.5" width="113" height="113" transform="rotate(0 80 80)"/>
      <rect x="23.5" y="23.5" width="113" height="113" transform="rotate(11.25 80 80)"/>
      <rect x="23.5" y="23.5" width="113" height="113" transform="rotate(22.5 80 80)"/>
      <rect x="23.5" y="23.5" width="113" height="113" transform="rotate(33.75 80 80)"/>
      <rect x="23.5" y="23.5" width="113" height="113" transform="rotate(45 80 80)"/>
      <rect x="23.5" y="23.5" width="113" height="113" transform="rotate(56.25 80 80)"/>
      <rect x="23.5" y="23.5" width="113" height="113" transform="rotate(67.5 80 80)"/>
      <rect x="23.5" y="23.5" width="113" height="113" transform="rotate(78.75 80 80)"/>
    </g>
    <circle cx="80" cy="80" r="70" fill="var(--red)"/>
  </svg>
  <div class="value-text">$2<sup>00</sup></div>

  <div class="coupon-number"><span>COUPON</span><span class="number-blank"></span></div>

  <h1 class="thanks">
    <span class="line1">Thank you</span>
    <span class="line2">for recommending us</span>
  </h1>

  <div class="food-photo" role="img" aria-label="Photo of a pepperoni, mushroom and olive pizza with a slice being lifted"></div>

  <footer class="info-band">
    <svg class="call-icon" viewBox="0 0 60 60" aria-hidden="true">
      <circle cx="30" cy="30" r="30" fill="var(--yellow)"/>
      <path d="M20 17c2-1 4 0 5 2l2 5c1 2 0 3-1 4l-2 2c1 3 4 6 7 7l2-2c1-1 2-2 4-1l5 2c2 1 3 3 2 5l-1 2c-1 2-3 3-6 2-9-2-17-10-19-19-1-3 0-5 2-6z" fill="var(--ink)"/>
      <path d="M32 18a10 10 0 0 1 10 10M32 13a15 15 0 0 1 15 15" fill="none" stroke="var(--ink)" stroke-width="2.5" stroke-linecap="round"/>
    </svg>
    <div class="order">
      <div class="order-label">ORDER NOW</div>
      <div class="order-phone">250 614 3750</div>
    </div>
    <div class="perks">
      <div class="perks-main">Fastest Delivery, Favourite Pizza for Sports teams etc.</div>
      <div class="perks-deal">Ask for group deals.</div>
    </div>
  </footer>
</main>
</body>
</html>
```